exciting cleaing project

I need a cleaning website built. It has to be built for a woman. the domain name is gwenshines.net.

I need the designer to find the images and code the site. the site needs to be about five pages.

here are some good examples:

https://www.tidypetal.com/gainesville/

http://abrightwren.com/

https://brisknookgainesville.com/services/

https://www.hevo.com/housekeepers/gainesville-fl

https://glintrow.com/

Target Market(s)

home cleaning,

Industry/Entity Type

Cleaning Service

Coding

Coded - Design and coding required

Number of Pages Required

4 page

Font styles to use
Script

Colors
33a6d7
85acd3
f04a50
ec1f27

Requirements
Must have
• nice design
Nice to have
• residential
Should not have
• commercial

```html
<!DOCTYPE html>
<html lang="en">
<head>
<meta charset="utf-8">
<title>Gwen Shines — Clean Home. Professional Service. Fair Price.</title>
<link rel="stylesheet" href="https://fonts.googleapis.com/css2?family=Great+Vibes&family=Montserrat:wght@300;400;600&display=swap">
<style>
:root{
  --red:#ec1f27;
  --coral:#f04a50;
  --sky:#33a6d7;
  --steel:#85acd3;
  --ink:#4a4f57;
  --muted:#8a9099;
  --faint:#e9ecf1;
  --pale-blue:#eef4fa;
  --paper:#ffffff;
  --canvas:#f4f5f7;
}
*{margin:0;padding:0;box-sizing:border-box}
html,body{width:1200px;height:4000px;overflow:hidden}
body{background:var(--canvas);font-family:"Montserrat",Arial,sans-serif;color:var(--ink);position:relative}
.page{position:absolute;left:150px;top:0;width:900px;height:3800px;background:var(--paper);overflow:hidden}
.abs{position:absolute}
.script{font-family:"Great Vibes",cursive;font-weight:400}
.photo{position:absolute}
.small{font-size:11px;line-height:1.6;color:var(--muted)}
.caps{text-transform:uppercase;letter-spacing:2px;font-size:10px;font-weight:600}

/* header */
.site-header{left:0;top:0;width:900px;height:64px;z-index:3}
.brand{left:28px;top:20px}
.brand-name{font-family:"Montserrat",Arial,sans-serif;font-size:17px;font-weight:600;letter-spacing:1px;color:var(--ink)}
.menu-toggle{right:30px;top:24px;width:22px}
.menu-toggle span{display:block;height:2px;background:var(--ink);margin-bottom:5px}

/* hero */
.hero{left:0;top:0;width:900px;height:600px;background:linear-gradient(180deg,#f7f8fa,#eceff3)}
.hero-photo{left:40px;top:60px;width:360px;height:520px;background:linear-gradient(160deg,#d9e6f2,#9fc3e2 60%,#c9d7e6)}
.hero-title{left:440px;top:250px;font-size:40px;font-weight:300;line-height:1.2;color:#8d939b}
.hero-title .accent{font-family:"Great Vibes",cursive;color:var(--coral);font-size:64px;display:block;margin-top:4px}

/* about */
.about-box{left:40px;top:650px;width:330px;height:250px;background:var(--pale-blue);padding:40px 34px}
.about-box .caps{color:var(--steel);margin-bottom:6px}
.about-box .script{color:#9fb6cc;font-size:46px;line-height:1}
.about-box .script.big{font-size:70px}
.about-plant{left:40px;top:900px;width:250px;height:230px;background:linear-gradient(160deg,#cfe3c8,#6fa56a 60%,#a8c79e)}
.about-copy{left:410px;top:670px;width:440px}
.about-copy .lead-label{font-size:11px;color:var(--muted);margin-bottom:18px}
.about-copy .lead{border-left:2px solid var(--steel);padding-left:18px;font-size:22px;font-weight:300;line-height:1.4;margin-bottom:26px}
.service-links{left:40px;top:1168px;width:820px;display:flex;justify-content:space-between;border-top:1px solid var(--faint);padding-top:10px}
.service-links span{font-size:8px;letter-spacing:1px;text-transform:uppercase;color:var(--muted)}

/* feature rows */
.feature-title{font-family:"Great Vibes",cursive;font-size:50px;line-height:1.1;color:#8fb3d6}
.feature-card{padding:28px 26px;width:350px}
.feature-card .icon{width:36px;height:36px;margin-bottom:12px}
.feature-card h3{font-size:11px;font-weight:600;letter-spacing:1px;text-transform:uppercase;margin-bottom:12px;line-height:1.5}
.feature-card p{font-size:10.5px;line-height:1.7}
.card-white{background:var(--paper);border:1px solid var(--faint);box-shadow:0 6px 18px rgba(0,0,0,.06)}
.card-white p{color:var(--muted)}
.card-red{background:var(--coral);color:#fff}
.card-blue{background:var(--steel);color:#fff}

/* band */
.band{left:0;top:2220px;width:900px;height:310px}
.band-text{left:0;top:2260px;width:900px;text-align:center;color:#fff}
.band-text .caps{font-size:11px}
.band-text .script{font-size:84px;line-height:1.05;opacity:.95}
.band-text .call{font-size:20px;letter-spacing:3px;font-weight:300;margin-top:4px}
.band-text .tiny{font-size:8px;margin-top:10px;opacity:.8}

/* testimonials */
.ghost{color:var(--faint);font-family:"Great Vibes",cursive;font-size:110px;line-height:1;text-align:center}
.testimonials-head{left:0;top:2570px;width:900px;text-align:center}
.testimonials-sub{left:0;top:2690px;width:900px;text-align:center;color:var(--muted)}
.quote{top:2725px;width:250px;height:140px;border:1px solid var(--faint);padding:20px;text-align:center}
.quote p{font-size:9.5px;line-height:1.6;color:var(--muted);margin-bottom:14px}
.quote .who{font-size:11px;font-weight:600;color:var(--ink)}
.quote .when{font-size:8.5px;color:var(--muted);margin-top:2px}

/* contact */
.contact-label{left:50px;top:2935px;color:var(--muted)}
.contact-ghost{left:40px;top:2955px;font-size:96px;line-height:1;color:#e4e8ee;font-family:"Great Vibes",cursive}
.contact-info{left:50px;top:3080px;width:340px;font-size:11px;line-height:2;color:var(--ink)}
.contact-info b{font-weight:600}
.hours{margin-top:30px}
.socials{left:50px;top:3330px;display:flex;gap:14px}
.socials span{width:16px;height:16px;border-radius:50%;background:#b9bec6;display:block}
.contact-form{left:470px;top:2948px;width:380px}
.field{margin-bottom:16px}
.field label{display:block;font-size:10px;color:var(--ink);margin-bottom:5px}
.field .req{color:var(--red)}
.field .box{height:26px;border:1px solid #dfe3e8;background:#fff}
.field .hint{font-size:8px;color:var(--muted);margin-top:3px}
.pair{display:flex;gap:12px}
.pair > div{flex:1}
.field .area{height:110px}
.send{display:inline-block;font-size:10px;padding:7px 16px;border:1px solid #ccd1d8;background:#f3f5f7}

/* footer */
.site-footer{left:0;top:3740px;width:900px;height:40px;background:var(--coral);color:#fff;display:flex;justify-content:space-between;align-items:center;padding:0 30px;font-size:9px}
</style>
</head>
<body>
<div class="page">

  <section class="abs hero">
    <div class="photo hero-photo" role="img" aria-label="Smiling cleaner in blue gloves holding cleaning supplies"></div>
    <h1 class="abs hero-title">Clean Home.<br>Professional Service.<span class="accent">Fair Price.</span></h1>
  </section>

  <header class="abs site-header">
    <div class="abs brand"><span class="brand-name">Gwen Shines</span></div>
    <div class="abs menu-toggle" aria-label="Menu"><span></span><span></span><span></span></div>
  </header>

  <section class="about">
    <div class="abs about-box">
      <div class="caps">About us</div>
      <div class="script">Reliable &amp;</div>
      <div class="script big">Honest</div>
    </div>
    <div class="photo about-plant" role="img" aria-label="Green leafy houseplant"></div>
    <div class="abs about-copy">
      <div class="lead-label">Our main attribute is quality of work</div>
      <div class="lead">to provide high quality services<br>for our valued clients.</div>
      <p class="small">We treat every home as if it were our own. Our friendly team arrives on time, brings its own supplies and leaves each room fresh, tidy and ready for you to relax. Trusted, insured and always easy to reach.</p>
    </div>
    <nav class="abs service-links">
      <span>Regular cleaning</span><span>Deep cleaning</span><span>Move in &amp; out</span><span>Kitchen care</span><span>Bathroom care</span><span>Custom plans</span>
    </nav>
  </section>

  <!-- attention to detail -->
  <div class="photo" style="left:40px;top:1240px;width:330px;height:260px;background:linear-gradient(150deg,#e6ecef,#9cc2b8 55%,#d6dfe2)" role="img" aria-label="Cleaner mopping a bright living room floor"></div>
  <div class="abs feature-title" style="left:560px;top:1230px">Attention to Detail</div>
  <div class="abs feature-card card-white" style="left:420px;top:1300px">
    <svg class="icon" viewBox="0 0 36 36"><rect x="3" y="6" width="30" height="26" rx="3" fill="none" stroke="var(--coral)" stroke-width="2"/><line x1="3" y1="13" x2="33" y2="13" stroke="var(--coral)" stroke-width="2"/><line x1="11" y1="3" x2="11" y2="9" stroke="var(--sky)" stroke-width="2"/><line x1="25" y1="3" x2="25" y2="9" stroke="var(--sky)" stroke-width="2"/><path d="M12 22l4 4 8-8" fill="none" stroke="var(--sky)" stroke-width="2"/></svg>
    <h3>Weekly, bi-weekly, monthly or<br>custom cleans available</h3>
    <p>Pick the schedule that fits your life. We keep the same trusted cleaner on your visits, follow your checklist and adjust the plan whenever your needs change.</p>
  </div>

  <!-- expert service -->
  <div class="abs feature-title" style="left:50px;top:1512px">Expert Service</div>
  <div class="abs feature-card card-red" style="left:40px;top:1592px;height:240px">
    <svg class="icon" viewBox="0 0 36 36"><rect x="4" y="12" width="28" height="18" rx="2" fill="none" stroke="#fff" stroke-width="2"/><path d="M4 12l14-8 14 8" fill="none" stroke="#fff" stroke-width="2"/><rect x="15" y="19" width="6" height="11" fill="#fff"/></svg>
    <h3>Move in &amp; out cleaning</h3>
    <p>Moving is stressful enough. We scrub cabinets, appliances, floors and fixtures so you can hand over the keys or settle into your new place with total peace of mind.</p>
  </div>
  <div class="photo" style="left:400px;top:1602px;width:460px;height:230px;background:linear-gradient(140deg,#cfe6f4,#4fa2d6 55%,#a9cfe8)" role="img" aria-label="Blue-gloved hands wiping a surface"></div>

  <!-- always prepared -->
  <div class="photo" style="left:40px;top:1890px;width:400px;height:300px;background:linear-gradient(150deg,#dfe3e6,#8fa3ad 55%,#cfd6da)" role="img" aria-label="Team cleaning a tiled kitchen seen from above"></div>
  <div class="abs feature-title" style="left:600px;top:1885px">Always Prepared</div>
  <div class="abs feature-card card-blue" style="left:480px;top:1960px;height:240px">
    <svg class="icon" viewBox="0 0 36 36"><rect x="3" y="6" width="30" height="26" rx="3" fill="none" stroke="#fff" stroke-width="2"/><line x1="3" y1="13" x2="33" y2="13" stroke="#fff" stroke-width="2"/><circle cx="18" cy="23" r="5" fill="var(--coral)"/></svg>
    <h3>Deep cleaning</h3>
    <p>Our deep clean reaches every corner: baseboards, vents, grout, inside the oven and behind the furniture. Perfect for spring, a special event or a fresh start at home.</p>
  </div>

  <!-- band -->
  <svg class="abs band" viewBox="0 0 900 310" preserveAspectRatio="none" role="img" aria-label="Red band over a bedroom scene">
    <defs><linearGradient id="bandFill" x1="0" y1="0" x2="0" y2="1"><stop offset="0" stop-color="#ef3f45"/><stop offset="1" stop-color="#e5262d"/></linearGradient></defs>
    <path d="M0 0H900V250C760 320 600 250 450 275S140 320 0 260Z" fill="url(#bandFill)"/>
  </svg>
  <div class="abs band-text">
    <div class="caps">Exceptional service</div>
    <div class="script">Modern Bedroom</div>
    <div class="call">CALL US 352-555-0148</div>
    <div class="tiny">Book a visit today · Free quote</div>
  </div>

  <!-- testimonials -->
  <div class="abs testimonials-head ghost">Testimonials</div>
  <div class="abs testimonials-sub caps" style="font-size:8px">What our clients say</div>
  <div class="abs quote" style="left:50px">
    <p>Always on time and incredibly thorough. My kitchen has never looked this good. I recommend them to every friend and neighbor.</p>
    <div class="who">Owen Pratt</div><div class="when">Client since June 2019</div>
  </div>
  <div class="abs quote" style="left:325px">
    <p>Friendly, careful and very easy to book. Coming home after a clean feels like checking into a lovely hotel every time.</p>
    <div class="who">Lena Hart</div><div class="when">Client since March 2020</div>
  </div>
  <div class="abs quote" style="left:600px">
    <p>They handled our move out clean quickly and we got our full deposit back. Honest people who truly care about details.</p>
    <div class="who">Cal Wexley</div><div class="when">Client since May 2021</div>
  </div>

  <!-- contact -->
  <div class="abs contact-label caps" style="font-size:8px">Get in touch</div>
  <div class="abs contact-ghost">Contact us</div>
  <div class="abs contact-info">
    <div><b>Phone:</b> 352-555-0148</div>
    <div><b>E-mail:</b> hello@gwenshines.net</div>
    <div><b>Address:</b> 210 Maple Lane, Gainesville, FL</div>
    <div class="hours"><b>Opening hours:</b></div>
    <div>Monday – Friday: 8am – 5pm</div>
    <div>Saturday: 9am – 1pm · Sunday: Closed</div>
  </div>
  <div class="abs socials"><span></span><span></span><span></span><span></span></div>

  <form class="abs contact-form">
    <div class="field"><label>Name <span class="req">*</span></label>
      <div class="pair"><div><div class="box"></div><div class="hint">First</div></div><div><div class="box"></div><div class="hint">Last</div></div></div>
    </div>
    <div class="field"><label>Phone</label><div class="box"></div></div>
    <div class="field"><label>Email <span class="req">*</span></label><div class="box"></div><div class="hint">Please enter a valid email address</div></div>
    <div class="field"><label>Address</label><div class="box"></div></div>
    <div class="field"><label>Subject</label><div class="box"></div></div>
    <div class="field"><label>Message <span class="req">*</span></label><div class="box area"></div></div>
    <span class="send">Send</span>
  </form>

  <footer class="abs site-footer">
    <span>© 2024 Gwen Shines. All rights reserved.</span>
    <span>Home · Services · Contact</span>
  </footer>
</div>
</body>
</html>
```